Business Card Design (NEW FILES)

ATTENTION: New vector files are available. Please update your design to reflect/use the new (better resolution) logo images.

Seeking a unique and professional business card design for a commercial drone photography/videography business. The layout should feature
the logo (attached) and include the following information:
978-512-6037
www.skyvantmedia.com
ORD Certified Remote Pilot

```html
<!DOCTYPE html>
<html lang="en">
<head>
<meta charset="utf-8">
<title>Skyvant Media – Business Card</title>
<link rel="stylesheet" href="https://fonts.googleapis.com/css2?family=Arimo:wght@400;700&display=swap">
<style>
  :root {
    --navy: #10163f;
    --orange: #e97b45;
    --white: #ffffff;
    --stage: #1b1b1d;
  }
  * { box-sizing: border-box; margin: 0; padding: 0; }
  html, body {
    width: 1200px; height: 963px; overflow: hidden;
    background: var(--stage);
    font-family: "Arimo", Arial, sans-serif;
  }
  .sheet { position: relative; width: 1200px; height: 963px; }
  .card {
    position: absolute; left: 250px; width: 700px; height: 400px;
    border-radius: 26px; overflow: hidden;
  }
  .card--front { top: 60px; background: var(--white); }
  .card--back {
    top: 503px; background: var(--navy);
    display: flex; align-items: center; justify-content: center;
  }

  /* front */
  .identity { position: absolute; left: 70px; top: 92px; padding-left: 22px; }
  .identity__flag {
    position: absolute; left: -52px; top: 2px; width: 40px; height: 44px;
    background: var(--orange);
  }
  .identity__name {
    font-weight: 700; font-size: 30px; letter-spacing: 0.5px;
    color: var(--navy); text-transform: uppercase;
  }
  .identity__name span { color: var(--orange); }
  .identity__role { font-size: 19px; color: var(--navy); margin-top: 2px; }

  .contact { position: absolute; left: 92px; top: 186px; list-style: none; }
  .contact li {
    display: flex; align-items: center; gap: 12px;
    font-size: 21px; color: var(--navy); margin-bottom: 14px;
  }
  .contact svg { width: 20px; height: 20px; flex: none; }

  .credentials {
    position: absolute; left: 92px; top: 300px;
    display: flex; align-items: center; gap: 22px;
  }
  .credentials__rule { width: 2px; height: 52px; background: var(--navy); transform: skewX(-20deg); }
  .credentials__text { font-size: 19px; line-height: 1.35; color: var(--navy); }

  .brand-mark {
    position: absolute; right: 48px; top: 60px;
    display: flex; align-items: center; gap: 12px;
  }
  .brand-mark__dot { width: 22px; height: 22px; border-radius: 50%; background: var(--orange); }
  .brand-mark__name {
    font-weight: 700; font-size: 30px; color: var(--navy);
    text-transform: uppercase; letter-spacing: 1px;
  }

  /* back */
  .back-brand { display: flex; align-items: center; gap: 16px; }
  .back-brand__dot { width: 30px; height: 30px; border-radius: 50%; background: var(--orange); }
  .back-brand__name {
    font-weight: 700; font-size: 52px; color: var(--white);
    text-transform: uppercase; letter-spacing: 3px;
  }
</style>
</head>
<body>
<main class="sheet">
  <section class="card card--front" aria-label="Card front">
    <div class="brand-mark">
      <span class="brand-mark__dot"></span>
      <span class="brand-mark__name">Skyvant Media</span>
    </div>

    <div class="identity">
      <span class="identity__flag"></span>
      <h1 class="identity__name">Mark <span>Doyle</span></h1>
      <p class="identity__role">Owner</p>
    </div>

    <ul class="contact">
      <li>
        <svg viewBox="0 0 24 24" aria-hidden="true"><path fill="var(--orange)" d="M6.6 10.8a15 15 0 0 0 6.6 6.6l2.2-2.2a1 1 0 0 1 1-.25 11.4 11.4 0 0 0 3.6.57 1 1 0 0 1 1 1V20a1 1 0 0 1-1 1A17 17 0 0 1 3 4a1 1 0 0 1 1-1h3.5a1 1 0 0 1 1 1c0 1.25.2 2.450.57 3.6a1 1 0 0 1-.25 1z"/></svg>
        978-512-6037
      </li>
      <li>
        <svg viewBox="0 0 24 24" aria-hidden="true"><g fill="none" stroke="var(--orange)" stroke-width="2"><circle cx="12" cy="12" r="9"/><ellipse cx="12" cy="12" rx="4" ry="9"/><path d="M3 12h18M5 7h14M5 17h14"/></g></svg>
        www.skyvantmedia.com
      </li>
    </ul>

    <div class="credentials">
      <span class="credentials__rule"></span>
      <p class="credentials__text">ORD Certified Remote Pilot<br>Fully Insured</p>
    </div>
  </section>

  <section class="card card--back" aria-label="Card back">
    <div class="back-brand">
      <span class="back-brand__dot"></span>
      <span class="back-brand__name">Skyvant Media</span>
    </div>
  </section>
</main>
</body>
</html>
```